Website Design for PawRank - New Digital Agency

We are creating a new digital marketing agency and need a new website. I have attached the logo. Our niche is going to be veterinarians. Use the same colors as in the logo (blue, white and gray).

I want real pictures of real people in this and not just boring stock photos. It needs to be related to the industry.

Home page (example:https://linkvorta.com/)
Service page (example: https://darvimosk.com/consulting/)
Case study page (example: https://www.tomaswellbry.com/seo/case-study/)

I will continue to update this brief.
Updates

I updated the brief with some additional sample sites 2 days ago and want to see more designs. I won't need that may more days ...just a few more.

Target Market(s)

veterinarians

Font styles to use
Sans Serif

Requirements
Must have
• I want a very clean looking site. Use the same colors as in the logo (blue, white and gray).
Nice to have
• We need to build this with the idea that the purpose is to generate leads for our business.
• Home page (example:https://linkvorta.com/)
• Service page (example: https://darvimosk.com/consulting/)
• Case study page (example: https://www.tomaswellbry.com/seo/case-study/)

```html
<!DOCTYPE html>
<html lang="en">
<head>
<meta charset="utf-8">
<title>PawRank – Digital Marketing for Veterinarians</title>
<link href="https://fonts.googleapis.com/css2?family=Poppins:wght@400;500;600;700&display=swap" rel="stylesheet">
<style>
:root{
  --blue:#1a5cc8;
  --blue-dark:#0f47a8;
  --blue-soft:#e4edfb;
  --navy:#0c1f3d;
  --ink:#1c1c1c;
  --grey:#6d6d6d;
  --grey-bg:#efefef;
  --grey-panel:#f5f5f5;
  --white:#ffffff;
}
*{margin:0;padding:0;box-sizing:border-box}
html,body{width:1200px;height:3871px;overflow:hidden;background:var(--white);font-family:'Poppins',sans-serif;color:var(--ink)}
.page{position:relative;width:1200px;height:3871px}
.abs{position:absolute}
.btn{position:absolute;background:var(--blue);color:var(--white);font-size:11px;font-weight:600;letter-spacing:.5px;display:flex;align-items:center;justify-content:center;text-transform:uppercase;box-shadow:0 4px 10px rgba(26,92,200,.3)}
.tick{display:block}
.section-title{position:absolute;left:0;width:1200px;text-align:center;font-size:27px;font-weight:700;text-transform:uppercase}
.tick-wrap{position:absolute;left:582px;width:36px;height:30px}

/* header */
.header{position:absolute;left:0;top:0;width:1200px;height:78px;background:var(--white)}
.brand{position:absolute;left:150px;top:22px;display:flex;align-items:center;gap:10px;font-size:28px;font-weight:700;color:var(--blue)}
.brand-dot{width:14px;height:14px;border-radius:50%;background:var(--blue)}
.nav{position:absolute;left:568px;top:38px;display:flex;gap:36px;font-size:11px;font-weight:500;text-transform:uppercase}
.login{left:975px;top:33px;width:74px;height:26px;box-shadow:none}

/* hero */
.hero-photo{position:absolute;left:44px;top:78px;width:1112px;height:542px;background:linear-gradient(100deg,#1a4fae 0%,#3d78cf 45%,#a9c3e6 80%,#d7e2f1 100%)}
.hero-edge{position:absolute;left:1180px;top:78px;width:20px;height:552px;background:var(--blue)}
.hero-title{position:absolute;left:150px;top:203px;font-size:48px;font-weight:600;color:var(--white);letter-spacing:1px}
.hero-text{position:absolute;left:150px;top:270px;width:390px;font-size:15px;line-height:28px;color:var(--white)}
.hero-btn{left:150px;top:373px;width:150px;height:44px;background:var(--navy);box-shadow:none}

/* services */
.services-bg{position:absolute;left:44px;top:632px;width:1112px;height:1148px;background:var(--grey-bg)}
.big-diamond{position:absolute;left:44px;top:438px}
.svc{position:absolute;width:212px;height:212px}
.svc::before{content:"";position:absolute;left:31px;top:31px;width:150px;height:150px;background:var(--blue-soft);transform:rotate(45deg)}
.svc-inner{position:absolute;inset:0;display:flex;flex-direction:column;align-items:center;justify-content:center;text-align:center;font-size:13px;font-weight:500;line-height:16px;gap:8px}
.svc-center::before{background:var(--white)}
.svc-kicker{font-size:12px;letter-spacing:1px;text-transform:uppercase}
.svc-head{font-size:23px;font-weight:600;text-transform:uppercase;line-height:24px}
.megaphone{position:absolute;left:44px;top:1105px;width:200px;height:160px;background:radial-gradient(circle at 30% 55%,#d63a3a 0%,#e9a4a4 35%,rgba(239,239,239,0) 70%)}

/* about */
.about-text{position:absolute;top:1415px;width:350px;font-size:13px;line-height:25px;color:var(--grey)}
.about-btn{left:563px;top:1518px;width:102px;height:34px}
.analysis{position:absolute;left:400px;top:1600px;width:400px;height:320px;background:radial-gradient(ellipse at center,#d9d9d9 0%,#ececec 55%,rgba(239,239,239,0) 75%);z-index:2}

/* blog */
.blog-bg{position:absolute;left:44px;top:1793px;width:1112px;height:380px;background:linear-gradient(90deg,#1650b8,#1f63cc)}
.edge-left{position:absolute;left:0;width:10px;background:var(--blue)}
.card{position:absolute;top:2059px;width:262px;height:285px;background:var(--white);box-shadow:0 6px 18px rgba(26,92,200,.18)}
.card-photo{position:absolute;left:18px;top:5px;width:226px;height:135px;border-radius:4px}
.card-date{position:absolute;left:18px;top:5px;width:36px;height:44px;background:var(--blue);color:var(--white);font-size:8px;line-height:10px;text-align:center;padding-top:6px;font-weight:600}
.card-title{position:absolute;left:0;top:158px;width:100%;text-align:center;font-size:13px;font-weight:600;line-height:17px}
.card-text{position:absolute;left:40px;top:200px;width:182px;text-align:center;font-size:10px;line-height:16px;color:var(--grey)}
.card-btn{left:93px;top:246px;width:76px;height:22px;font-size:10px;text-transform:none;box-shadow:none}

/* team */
.team-bg{position:absolute;left:44px;top:2405px;width:1112px;height:647px;background:var(--grey-panel)}
.member{position:absolute;top:2598px;width:220px;height:286px}
.member-photo{position:absolute;inset:0}
.member-name{position:absolute;left:0;bottom:0;width:100%;height:30px;background:rgba(40,40,40,.85);color:var(--white);font-size:11px;display:flex;align-items:center;justify-content:center}
.team-btn{left:536px;top:2940px;width:130px;height:36px}

/* contact */
.contact-left{position:absolute;left:44px;top:3096px;width:557px;height:495px;background:linear-gradient(135deg,#1f62cc,#3a7ad6)}
.contact-right{position:absolute;left:601px;top:3096px;width:555px;height:495px;background:linear-gradient(135deg,#1352bd,#1a5cc8)}
.contact-h{position:absolute;top:3163px;font-size:27px;font-weight:600;color:var(--white);text-transform:uppercase}
.field{position:absolute;left:150px;width:294px;height:40px;border-bottom:1px solid rgba(255,255,255,.6);color:var(--white);font-size:11px;display:flex;align-items:flex-start;padding-top:6px}
.submit{left:150px;top:3477px;width:130px;height:40px;background:#0a0a0a;box-shadow:none}
.info-text{position:absolute;left:651px;top:3215px;width:310px;font-size:12px;line-height:24px;color:var(--white)}
.info-row{position:absolute;left:651px;display:flex;align-items:center;gap:20px;font-size:12px;color:var(--white)}
.info-icon{width:30px;height:30px;display:flex;align-items:center;justify-content:center;position:relative}
.info-icon::before{content:"";position:absolute;width:24px;height:24px;background:rgba(255,255,255,.15);transform:rotate(45deg)}
.info-icon svg{position:relative}

/* footer */
.footer{position:absolute;left:44px;top:3625px;width:1112px;height:220px;background:var(--grey-panel)}
.foot-nav{position:absolute;left:150px;top:3671px;display:flex;gap:32px;font-size:11px;text-transform:uppercase;color:#333}
.foot-line{position:absolute;left:150px;top:3728px;width:900px;height:1px;background:#d6d6d6}
.social{position:absolute;top:3692px;width:26px;height:26px;border:1px solid #9a9a9a;transform:rotate(45deg)}
.copy{position:absolute;left:188px;top:3772px;font-size:11px;color:#444}
.copy b{color:var(--blue);font-weight:500}
.foot-links{position:absolute;top:3772px;font-size:11px;color:#444}
</style>
</head>
<body>
<div class="page">

  <!-- header -->
  <header class="header">
    <div class="brand"><span class="brand-dot"></span>PawRank</div>
    <nav class="nav"><span>Home</span><span>About us</span><span>Our services</span><span>Contact</span><span>Blog</span></nav>
    <div class="btn login">Login</div>
  </header>

  <!-- hero -->
  <div class="hero-edge"></div>
  <div class="hero-photo" role="img" aria-label="Photo of a thoughtful woman at a desk in a bright office, tinted blue"></div>
  <h1 class="hero-title">WE ACCELERATE</h1>
  <p class="hero-text">Lorem Ipsum is simply dummy text of the printing and typesetting industry. Lorem Ipsum has been the indu</p>
  <div class="btn hero-btn">Contact us</div>

  <!-- services -->
  <div class="services-bg"></div>
  <svg class="big-diamond" width="1112" height="1344" viewBox="44 438 1112 1344">
    <polygon points="600,438 1272,1110 600,1782 -72,1110" fill="#f8f8f8"/>
  </svg>

  <div class="svc" style="left:494px;top:552px"><div class="svc-inner">
    <svg width="34" height="34" viewBox="0 0 34 34" fill="none" stroke="#1c1c1c" stroke-width="1.6"><path d="M4 6h26l-10 12v10l-6 3V18z"/></svg>
    <span>Funnel<br>Marketing</span></div></div>

  <div class="svc" style="left:366px;top:681px"><div class="svc-inner">
    <svg width="36" height="32" viewBox="0 0 36 32" fill="none" stroke="#1c1c1c" stroke-width="1.6"><rect x="3" y="3" width="30" height="20" rx="1"/><path d="M13 29h10M18 23v6"/><circle cx="18" cy="13" r="4" stroke="#1a5cc8"/></svg>
    <span>Landing<br>Pages</span></div></div>

  <div class="svc" style="left:622px;top:681px"><div class="svc-inner">
    <svg width="34" height="32" viewBox="0 0 34 32" fill="none" stroke="#1c1c1c" stroke-width="1.8"><path d="M5 28V18M13 28V10M21 28V14M29 28V5"/></svg>
    <span>Paid Search<br>Ads</span></div></div>

  <div class="svc" style="left:242px;top:810px"><div class="svc-inner">
    <svg width="34" height="34" viewBox="0 0 34 34" fill="none" stroke="#1c1c1c" stroke-width="1.6"><rect x="4" y="4" width="12" height="10"/><rect x="18" y="18" width="12" height="10" stroke="#1a5cc8"/><path d="M10 14v10h8M24 18V9h-8"/></svg>
    <span>Social<br>Marketing</span></div></div>

  <div class="svc svc-center" style="left:494px;top:810px"><div class="svc-inner" style="gap:4px">
    <span class="svc-kicker">Marketing</span><span class="svc-head">Services</span>
    <svg class="tick" width="30" height="24" viewBox="0 0 30 24"><path d="M2 12l9 9L28 2l-17 13z" fill="#1a5cc8"/></svg></div></div>

  <div class="svc" style="left:746px;top:810px"><div class="svc-inner">
    <svg width="34" height="34" viewBox="0 0 34 34" fill="none" stroke="#1c1c1c" stroke-width="1.8"><circle cx="14" cy="14" r="10"/><path d="M21 21l9 9"/><circle cx="14" cy="14" r="4" stroke="#1a5cc8"/></svg>
    <span>SEO<br>Optimisation</span></div></div>

  <div class="svc" style="left:494px;top:1029px"><div class="svc-inner">
    <svg width="36" height="30" viewBox="0 0 36 30" fill="none" stroke="#1c1c1c" stroke-width="1.6"><rect x="3" y="5" width="30" height="21"/><path d="M3 5l15 12L33 5"/></svg>
    <span>Email<br>Marketing</span></div></div>

  <div class="megaphone" role="img" aria-label="Illustration of a red megaphone with small chart and target icons"></div>

  <!-- about -->
  <h2 class="section-title" style="top:1318px">About us</h2>
  <svg class="tick-wrap" style="top:1362px" viewBox="0 0 30 24"><path d="M2 12l9 9L28 2l-17 13z" fill="#1a5cc8"/></svg>
  <p class="about-text" style="left:237px">Lorem Ipsum is simply dummy text of the printing and typesetting industry. Lorem Ipsum been the standard dummy text ever since book.</p>
  <p class="about-text" style="left:620px">Lorem Ipsum is simply dummy text of the printing and typesetting industry. Lorem Ipsum been the standard dummy text ever since book.</p>
  <div class="btn about-btn">Read more</div>

  <!-- blog -->
  <div class="edge-left" style="top:1767px;height:430px"></div>
  <div class="edge-left" style="left:1190px;top:1767px;height:430px"></div>
  <div class="blog-bg"></div>
  <div class="analysis" role="img" aria-label="Sketch illustration of hands around notes on analysis and digital marketing"></div>
  <h2 class="section-title" style="top:1955px;color:var(--white)">Blog</h2>
  <svg class="tick-wrap" style="top:1996px" viewBox="0 0 30 24"><path d="M2 12l9 9L28 2l-17 13z" fill="#ffffff"/></svg>

  <article class="card" style="left:186px">
    <div class="card-photo" role="img" aria-label="Photo of a woman reading in a warm room" style="background:linear-gradient(135deg,#c98a5d,#6e4a36)"></div>
    <div class="card-date">20<br>Jan<br>2019</div>
    <h3 class="card-title">There are many variations<br>of passages have</h3>
    <p class="card-text">Lorem Ipsum is simply dummy text of the printing and</p>
    <div class="btn card-btn">Read More</div>
  </article>
  <article class="card" style="left:470px">
    <div class="card-photo" role="img" aria-label="Photo of a group of colleagues smiling together" style="background:linear-gradient(135deg,#cfd4da,#7d8690)"></div>
    <div class="card-date">20<br>Jan<br>2019</div>
    <h3 class="card-title">There are many variations<br>of passages have</h3>
    <p class="card-text">Lorem Ipsum is simply dummy text of the printing and</p>
    <div class="btn card-btn">Read More</div>
  </article>
  <article class="card" style="left:754px">
    <div class="card-photo" role="img" aria-label="Photo of people meeting in a dim cafe" style="background:linear-gradient(135deg,#5a4a3a,#1e1b18)"></div>
    <div class="card-date">20<br>Jan<br>2019</div>
    <h3 class="card-title">There are many variations<br>of passages have</h3>
    <p class="card-text">Lorem Ipsum is simply dummy text of the printing and</p>
    <div class="btn card-btn">Read More</div>
  </article>

  <!-- team -->
  <div class="team-bg"></div>
  <h2 class="section-title" style="top:2464px">Our Tem</h2>
  <svg class="tick-wrap" style="top:2506px" viewBox="0 0 30 24"><path d="M2 12l9 9L28 2l-17 13z" fill="#1a5cc8"/></svg>
  <div class="member" style="left:217px"><div class="member-photo" role="img" aria-label="Portrait photo of a smiling team member in a red shirt" style="background:linear-gradient(180deg,#3c3c3c,#b3262c)"></div><div class="member-name">Omar Kessling</div></div>
  <div class="member" style="left:490px"><div class="member-photo" role="img" aria-label="Portrait photo of a smiling team member in a light blue shirt" style="background:linear-gradient(180deg,#2b2b2b,#9fb5cc)"></div><div class="member-name">Ren Takoda</div></div>
  <div class="member" style="left:764px"><div class="member-photo" role="img" aria-label="Portrait photo of a bearded team member in a dark shirt" style="background:linear-gradient(180deg,#bfc4c8,#2c2c2c)"></div><div class="member-name">Ivo Brandt</div></div>
  <div class="btn team-btn">Read more</div>

  <!-- contact -->
  <div class="edge-left" style="top:3060px;height:535px"></div>
  <div class="edge-left" style="left:1190px;top:3060px;height:535px"></div>
  <div class="contact-left"></div>
  <div class="contact-right"></div>
  <svg class="abs" style="left:540px;top:3530px" width="122" height="61" viewBox="0 0 122 61"><polygon points="0,61 61,0 122,61" fill="#ffffff"/></svg>

  <svg class="abs" style="left:150px;top:3132px" width="22" height="18" viewBox="0 0 30 24"><path d="M2 12l9 9L28 2l-17 13z" fill="#ffffff"/></svg>
  <h2 class="contact-h" style="left:150px">Quick contact</h2>
  <div class="field" style="top:3230px">Name</div>
  <div class="field" style="top:3277px">Email</div>
  <div class="field" style="top:3324px">Phone</div>
  <div class="field" style="top:3371px;height:60px">Message</div>
  <div class="btn submit">Submit now</div>

  <svg class="abs" style="left:651px;top:3132px" width="22" height="18" viewBox="0 0 30 24"><path d="M2 12l9 9L28 2l-17 13z" fill="#ffffff"/></svg>
  <h2 class="contact-h" style="left:651px">Contact info</h2>
  <p class="info-text">Lorem Ipsum is simply dummy text of the printing and typesetting industry. Lorem Ipsum has been.</p>
  <div class="info-row" style="top:3302px"><span class="info-icon"><svg width="12" height="16" viewBox="0 0 12 16"><path d="M6 0a6 6 0 0 0-6 6c0 4.5 6 10 6 10s6-5.5 6-10a6 6 0 0 0-6-6zm0 8.5A2.5 2.5 0 1 1 6 3.5a2.5 2.5 0 0 1 0 5z" fill="#fff"/></svg></span>48 Marlow Lane Fenbrook</div>
  <div class="info-row" style="top:3360px"><span class="info-icon"><svg width="14" height="14" viewBox="0 0 14 14"><path d="M3 0l3 3-2 2c1 2 3 4 5 5l2-2 3 3-2 3C6 14 0 8 0 2z" fill="#fff"/></svg></span>+1-310-555-0172</div>
  <div class="info-row" style="top:3418px"><span class="info-icon"><svg width="14" height="11" viewBox="0 0 14 11"><rect width="14" height="11" fill="#fff"/><path d="M0 0l7 6 7-6" fill="none" stroke="#1a5cc8" stroke-width="1.3"/></svg></span>hello@pawrank.com</div>

  <!-- footer -->
  <footer class="footer"></footer>
  <nav class="foot-nav"><span>Home</span><span>About</span><span>Services</span><span>Contact</span><span>Blog</span></nav>
  <span class="social" style="left:920px"></span>
  <span class="social" style="left:970px"></span>
  <span class="social" style="left:1020px"></span>
  <div class="foot-line"></div>
  <svg class="abs" style="left:150px;top:3770px" width="24" height="20" viewBox="0 0 30 24"><path d="M2 12l9 9L28 2l-17 13z" fill="#1a5cc8"/></svg>
  <p class="copy">@ Copyright 2019 <b>PAWRANK</b></p>
  <p class="foot-links" style="left:826px">Terms of Service</p>
  <p class="foot-links" style="left:972px">Privacy Policy</p>

</div>
</body>
</html>
```